Bref créative
Business Cards, Stationery and Email signature for Luxury Brand
Kestral
I need double sided standard sized Business Card [3.5" x 2"]
Can use whatever font will look high end
Professional
Dennis L. Farrow
CEO/President
417 Larkspur Ave.
Suite 350
Beverly Hills, CA 90187
df@kestralinquiries.example
kestralinquiries.example
Please put in holder for this - Don't have number yet
Want to have plastic business card. All black on front of card with just logo. Back of Card will have all information. Black border on back might be nice showing starburst from logo on top and having line under logo on bottom border of card. Open to other ideas for back as well.
ALL INFORMATION WILL GO ON BACK OF CARD - Card will be plastic
Logo only on front

```html
<!DOCTYPE html>
<html lang="en">
<head>
<meta charset="utf-8">
<title>Kestral Business Card</title>
<link rel="stylesheet" href="https://fonts.googleapis.com/css2?family=Didact+Gothic&display=swap">
<style>
  :root {
    --backdrop: #1c1c1e;
    --card-black: #0b0b0c;
    --card-black-edge: #2a2a2d;
    --card-white: #f1f1f1;
    --card-grey: #bdbdbd;
    --silver: #d9d9d9;
    --ink-dark: #1a1a1a;
    --ink-light: #eaeaea;
    --ink-muted: #9a9a9a;
  }
  html, body {
    margin: 0;
    width: 1200px;
    height: 901px;
    overflow: hidden;
    background: var(--backdrop);
    font-family: "Didact Gothic", "Century Gothic", sans-serif;
  }
  .canvas {
    position: relative;
    width: 1200px;
    height: 901px;
    display: flex;
    align-items: center;
    justify-content: center;
    gap: 60px;
  }
  .card {
    position: relative;
    width: 520px;
    height: 297px;
    border-radius: 6px;
    overflow: hidden;
    box-shadow: 0 14px 30px rgba(0,0,0,0.55);
  }
  /* Front */
  .card-front {
    background: radial-gradient(ellipse at 50% 45%, #26262a 0%, var(--card-black) 65%);
    border: 1px solid var(--card-black-edge);
  }
  .card-front .frame {
    position: absolute;
    inset: 14px;
    border: 1px solid rgba(217,217,217,0.35);
    border-radius: 3px;
  }
  .brand {
    position: absolute;
    left: 0; right: 0;
    text-align: center;
    color: var(--ink-light);
    letter-spacing: 6px;
    text-transform: uppercase;
  }
  .card-front .brand { top: 118px; font-size: 38px; }
  .card-front .web {
    position: absolute;
    left: 0; right: 0;
    top: 172px;
    text-align: center;
    font-size: 11px;
    color: var(--ink-muted);
    letter-spacing: 1px;
  }
  /* Back */
  .card-back {
    background: linear-gradient(90deg, var(--card-grey) 0%, var(--card-white) 12%, var(--card-white) 88%, var(--card-grey) 100%);
  }
  .card-back .name {
    position: absolute;
    left: 0; right: 0;
    top: 46px;
    text-align: center;
    font-size: 19px;
    color: var(--ink-dark);
  }
  .card-back .title {
    position: absolute;
    left: 0; right: 0;
    top: 70px;
    text-align: center;
    font-size: 11px;
    color: #444;
  }
  .band {
    position: absolute;
    left: 0; right: 0;
    top: 94px;
    height: 110px;
    background: radial-gradient(ellipse at 50% 45%, #2a2a2e 0%, var(--card-black) 70%);
    border-top: 2px solid var(--silver);
    border-bottom: 2px solid var(--silver);
  }
  .band .brand { top: 34px; font-size: 32px; }
  .contact {
    position: absolute;
    left: 0; right: 0;
    top: 214px;
    text-align: center;
    font-size: 11.5px;
    line-height: 1.5;
    color: var(--ink-dark);
  }
</style>
</head>
<body>
<main class="canvas">
  <section class="card card-front" aria-label="Card front">
    <div class="frame"></div>
    <div class="brand">Kestral</div>
    <div class="web">kestralinquiries.example</div>
  </section>

  <section class="card card-back" aria-label="Card back">
    <div class="name">Dennis L. Farrow</div>
    <div class="title">CEO/President</div>
    <div class="band">
      <div class="brand">Kestral</div>
    </div>
    <div class="contact">
      417 Larkspur Ave. Suite 350, Beverly Hills, CA 90187<br>
      Toll Free : 800-240-1187, Phone : 310-555-0142<br>
      df@kestralinquiries.example
    </div>
  </section>
</main>
</body>
</html>
```